Financing Pitch Deck

PowerPoint presentation for meeting next week. Please include the Veltra Logo, the Harrowby KT logo, and the Quorvex Ambassador Logo. Recall, Anselm is an Quorvex ambassador.
Please alter Slide 2 to read identify not identifies:

ROQ Text Modeling Algorithms employ randomness to Identify Distinctive Word Combinations

```html
<!DOCTYPE html>
<html lang="en">
<head>
<meta charset="utf-8">
<title>Veltra – 2021 Financing Pitch Deck</title>
<link href="https://fonts.googleapis.com/css2?family=Carlito:wght@400;700&family=Saira+Semi+Condensed:wght@600&family=Signika:wght@600&display=swap" rel="stylesheet">
<style>
:root{
  --blue:#1cb4e3;
  --title-blue:#27a6dc;
  --green:#25dc8c;
  --teal:#2bb59b;
  --circle-blue:#2aa1d6;
  --navy:#1c4566;
  --ink:#2b2b2b;
  --grey:#8e8e8e;
  --pale-blue:#c5e5f4;
  --black:#000;
  --white:#fff;
}
*{margin:0;padding:0;box-sizing:border-box}
html,body{width:1200px;height:2194px;overflow:hidden;background:var(--white)}
body{position:relative;font-family:"Carlito",sans-serif;color:var(--ink)}
.slide{position:absolute;left:251px;width:696px;height:393px;background:var(--white);overflow:hidden;box-shadow:14px 14px 26px rgba(0,0,0,.28)}
.s1{top:60px}.s2{top:480px}.s3{top:899px}.s4{top:1318px}.s5{top:1736px}
.abs{position:absolute}
.brand{position:absolute;display:flex;align-items:center;gap:7px;font-family:"Carlito",sans-serif;font-size:21px;color:var(--blue);line-height:1}
.brand-dot{width:16px;height:16px;border-radius:50%;background:var(--green)}
.footer-url{position:absolute;left:49px;bottom:8px;font-size:6px;color:#a9a9a9}
.page-no{position:absolute;right:36px;bottom:8px;font-size:6px;color:#a9a9a9}

/* slide 1 */
.s1 .bg{position:absolute;inset:0;background:radial-gradient(circle at 30% 40%,#f3fbf7,#eef6f9 60%,#f7fafb)}
.year{position:absolute;left:44px;top:100px;width:280px;height:160px;overflow:visible}
.year text{font-family:"Saira Semi Condensed",sans-serif;font-weight:600;font-size:180px}
.s1 .brand{left:362px;top:112px;font-size:30px}
.s1 .brand-dot{width:22px;height:22px}
.deck-title{right:144px;top:153px;text-align:right;font-family:"Signika",sans-serif;font-weight:600;color:var(--navy);font-size:45px;line-height:59px}
.presenter{right:144px;top:291px;text-align:right;font-size:13px;color:var(--title-blue);line-height:16px;font-weight:400}
.badge{position:absolute;left:595px;width:60px}
.badge-a{top:115px;height:60px;background:#6a9fd1}
.badge-b{top:178px;height:55px;background:#eef1f5;border:1px solid #dfe3e8}
.badge-c{top:235px;height:60px;background:var(--black);border:1px solid #d0d0d0}

/* dark band slides */
.band{position:absolute;left:0;top:0;width:100%;height:196px;background:var(--black)}
.s2 .brand{left:51px;top:32px;font-size:19px}
.s2 .brand-dot{width:14px;height:14px}
.intro-title{left:53px;top:78px;font-size:55px;color:var(--blue);font-weight:400;line-height:1}
.fact{position:absolute;top:53px;width:121px;height:121px;border-radius:50%;display:flex;align-items:center;justify-content:center;text-align:center;color:var(--white);font-size:11.5px;line-height:15.5px;padding:0 18px}
.fact-a{left:405px;background:var(--circle-blue)}
.fact-b{left:544px;background:var(--teal)}
.intro-lead{left:53px;top:219px;width:182px;font-size:20px;line-height:26px;color:var(--title-blue)}
.steps{position:absolute;left:287px;top:224px;width:362px;list-style:none}
.steps li{display:flex;gap:10px;align-items:flex-start;font-size:11.6px;line-height:14px;text-align:justify;margin-bottom:12px}
.steps li:nth-child(2){margin-top:4px}
.step-no{flex:0 0 32px;height:32px;border-radius:50%;background:var(--green);color:var(--white);font-size:11px;display:flex;align-items:center;justify-content:center}

/* slide 3 */
.tower{position:absolute;inset:0}
.s3 .brand{left:538px;top:25px}
.s3 .brand-dot{width:18px;height:18px}
.unique-title{left:53px;top:68px;font-size:54px;line-height:57px;color:var(--title-blue);font-weight:400}
.points{position:absolute;left:48px;top:211px;width:340px;list-style:none}
.points li{display:flex;gap:14px;font-size:16.5px;line-height:19px;color:#333;margin-bottom:34px}
.points li::before{content:"";flex:0 0 32px;height:32px;border-radius:50%;background:var(--blue)}
.allows{left:427px;top:209px;font-size:16.5px;color:#333}
.gains{position:absolute;left:427px;top:252px;list-style:none;font-size:16.5px;line-height:29px;color:#333}
.gains li::before{content:"•";margin-right:9px;font-size:15px;vertical-align:top;position:relative;top:-2px}

/* slide 4 */
.s4 .net{position:absolute;inset:0;background:radial-gradient(circle at 20% 30%,#f4f5f6,#fbfbfc 60%,#fff)}
.s4 .brand{left:538px;top:22px}
.s4 .brand-dot{width:18px;height:18px}
.notable-title{left:53px;top:101px;font-size:55px;line-height:65px;color:var(--blue);font-weight:400}
.algos{position:absolute;left:374px;top:83px;width:284px;list-style:none}
.algos li{display:flex;gap:10px;margin-bottom:14px}
.algos li::before{content:"";flex:0 0 31px;height:31px;border-radius:50%;background:var(--blue)}
.algo-name{display:block;font-size:14px;color:#111;line-height:17px}
.algo-desc{display:block;font-size:12.3px;line-height:15.5px;color:#333}

/* slide 5 */
.s5 .brand{left:538px;top:22px}
.s5 .brand-dot{width:18px;height:18px}
.team-title{left:53px;top:42px;font-size:52px;color:var(--blue);line-height:1;font-weight:400}
.member{position:absolute;top:124px;width:170px;text-align:center}
.portrait{display:block;width:143px;height:143px;margin:0 auto;border-radius:50%;border:3px solid var(--white);background:radial-gradient(circle at 50% 38%,#c9a891 0 22%,#ececec 23% 55%,#2c3440 56%)}
.member-name{display:block;margin-top:14px;font-size:14.5px;color:#8a8a8a}
.member-role{display:block;font-size:10px;line-height:12px;color:#9a9a9a}
.m1{left:68px}.m2{left:264px}.m3{left:459px}
</style>
</head>
<body>

<section class="slide s1" aria-label="Title slide">
  <div class="bg" role="img" aria-label="Soft pale pattern of overlapping circles"></div>
  <svg class="year" viewBox="0 0 280 160" aria-label="2021">
    <defs>
      <linearGradient id="yearTone" x1="0" y1="0" x2="1" y2="0">
        <stop offset=".1" stop-color="#1cb4e3"/>
        <stop offset=".9" stop-color="#25dc8c"/>
      </linearGradient>
    </defs>
    <text x="4" y="150" textLength="268" lengthAdjust="spacingAndGlyphs" fill="url(#yearTone)">2021</text>
  </svg>
  <div class="brand"><span class="brand-dot"></span>Veltra</div>
  <h1 class="abs deck-title">Financing<br>Pitch Deck</h1>
  <p class="abs presenter">Presenter: John Edwdard Doe<br>Dec 20, 2021</p>
  <div class="badge badge-a" role="img" aria-label="Harrowby KT badge"></div>
  <div class="badge badge-b" role="img" aria-label="Builders and innovators listing badge"></div>
  <div class="badge badge-c" role="img" aria-label="Quorvex Ambassador 2021 badge"></div>
</section>

<section class="slide s2" aria-label="Introduction">
  <div class="band"></div>
  <div class="brand"><span class="brand-dot"></span>Veltra</div>
  <h2 class="abs intro-title">Introduction</h2>
  <div class="fact fact-a">Veltra IP (ROQ) is a specialty AI company founded in 2015</div>
  <div class="fact fact-b">ROQ is a single member LLC owned by Veltra Analytics</div>
  <p class="abs intro-lead">ROQ has developed a collection of specialty algorithms which have the capacity to:</p>
  <ol class="steps">
    <li><span class="step-no">1</span><span>Advance the effectiveness of all existing linguistic artificial intelligence beyond the theoretical limits to which such algorithms are currently subject, to near perfection.</span></li>
    <li><span class="step-no">2</span><span>Derive benefit from the use of true random in a quantum environment.</span></li>
    <li><span class="step-no">3</span><span>These attributes may make ROQ one of the most important technology companies in the world at present.</span></li>
  </ol>
  <span class="footer-url">veltraanalytics.com</span>
  <span class="page-no">2</span>
</section>

<section class="slide s3" aria-label="Why is ROQ Text Modelling Unique">
  <svg class="tower" width="696" height="393" viewBox="0 0 696 393">
    <defs>
      <linearGradient id="towerTone" x1="0" y1="1" x2="1" y2="0">
        <stop offset="0" stop-color="#ffffff"/>
        <stop offset=".5" stop-color="#e6eef3"/>
        <stop offset="1" stop-color="#f3f7f9"/>
      </linearGradient>
    </defs>
    <polygon role="img" aria-label="Photo of a glass office tower" points="460,0 696,0 696,393 320,393" fill="url(#towerTone)"/>
    <polygon points="696,0 696,393 540,393" fill="var(--pale-blue)"/>
  </svg>
  <div class="brand"><span class="brand-dot"></span>Veltra</div>
  <h2 class="abs unique-title">Why is ROQ Text<br>Modelling Unique</h2>
  <ul class="points">
    <li>ROQ Algorithms systematically employ randomness in multiple ways</li>
    <li>ROQ Text Modeling Algorithms employ randomness to Identify Distinctive Word Combinations</li>
  </ul>
  <p class="abs allows">This allows us to:</p>
  <ul class="gains">
    <li>Detect weak signals in data,</li>
    <li>Train models efficiently, and</li>
    <li>Eliminate virtually all noise</li>
  </ul>
  <span class="footer-url">veltraanalytics.com</span>
</section>

<section class="slide s4" aria-label="Other Notable Algorithms">
  <div class="net" role="img" aria-label="Faint network of connected nodes"></div>
  <div class="brand"><span class="brand-dot"></span>Veltra</div>
  <h2 class="abs notable-title">Other<br>Notable<br>Algorithms</h2>
  <ul class="algos">
    <li><div><span class="algo-name">Nx Name Extraction—</span><span class="algo-desc">Identifies names of individuals in text with greater accuracy than most competing algorithms and 300x faster than ARLO.</span></div></li>
    <li><div><span class="algo-name">Data Lake Indexer—</span><span class="algo-desc">Indexes data and maintains speed regardless of the size of dataset processed and slows only linearly as the number of words per query grows, unlike any competing indexing algorithm.</span></div></li>
    <li><div><span class="algo-name">Back Propagation—</span><span class="algo-desc">Doubles speed of training neural networks.</span></div></li>
  </ul>
</section>

<section class="slide s5" aria-label="Leadership Team">
  <div class="band"></div>
  <div class="brand"><span class="brand-dot"></span>Veltra</div>
  <h2 class="abs team-title">Leadership Team</h2>
  <div class="member m1">
    <span class="portrait" role="img" aria-label="Portrait of Rowan Pell"></span>
    <span class="member-name">Rowan Pell</span>
    <span class="member-role">Interim CEO</span>
  </div>
  <div class="member m2">
    <span class="portrait" role="img" aria-label="Portrait of Dr. Anselm Vossberg"></span>
    <span class="member-name">Dr. Anselm Vossberg</span>
    <span class="member-role">Chief Data Scientist &amp; Co-<br>Founder</span>
  </div>
  <div class="member m3">
    <span class="portrait" role="img" aria-label="Portrait of Corwin Hale"></span>
    <span class="member-name">Corwin Hale</span>
    <span class="member-role">Senior Vice President, General<br>Counsel &amp; Co-Founder</span>
  </div>
  <span class="footer-url">veltraanalytics.com</span>
  <span class="page-no">5</span>
</section>

</body>
</html>
```